Need a new letterhead

Need a new fresh exciting letterhead. Remove the footer...info is outdated.

Target Market(s)

B2B

Industry/Entity Type

Electrical Power

Colors

Designer to choose colors to be used in the design.

Requirements
Must have
• Red and Blue Brindlecroft Arcwell Logo
Nice to have
• Powering a greener tomorrow in footer...reorganize the words?

```html
<!DOCTYPE html>
<html lang="en">
<head>
<meta charset="utf-8">
<title>Brindlecroft Arcwell – Letterhead &amp; Envelope</title>
<link href="https://fonts.googleapis.com/css2?family=Open+Sans:wght@400;600;700&family=Lato:wght@400;700&display=swap" rel="stylesheet">
<style>
  :root{
    --brand-red:#ee0a1d;
    --brand-blue:#1a2a8c;
    --ink:#3c3c3c;
    --ink-soft:#555;
    --paper:#ffffff;
    --backdrop:#e4e4e4;
    --rule:#9a9a9a;
    --tag-green:#3aa935;
  }
  *{box-sizing:border-box;margin:0;padding:0}
  html,body{width:1200px;height:1200px;overflow:hidden;background:var(--backdrop)}
  body{position:relative;font-family:"Open Sans",Arial,sans-serif;color:var(--ink)}

  .sheet{position:absolute;background:var(--paper);box-shadow:0 2px 8px rgba(0,0,0,.18)}
  .edge-bar{position:absolute;left:0;top:0;bottom:0;background:var(--brand-red)}

  /* Letterhead */
  .letterhead{left:60px;top:110px;width:640px;height:828px}
  .letterhead .edge-bar{width:12px}
  .brand-name{position:absolute;font-family:"Open Sans",Arial,sans-serif;font-weight:700;color:var(--brand-red);line-height:1.05;letter-spacing:.3px}
  .letterhead .brand-name{left:60px;top:26px;font-size:21px}
  .contact-block{position:absolute;left:428px;top:16px;padding-left:13px;border-left:1px solid var(--rule);font-size:10.5px;line-height:11.6px;color:var(--ink-soft);font-style:normal}
  .contact-block .gap{height:6px}
  .label{color:var(--brand-red);font-weight:700}
  .web{color:var(--brand-blue)}
  .web .tld{color:var(--brand-red)}

  .letter-body{position:absolute;left:60px;top:148px;width:520px;font-size:10.3px;line-height:18.4px;color:var(--ink-soft)}
  .letter-body p{margin-bottom:18.4px}
  .recipient{line-height:12.4px}
  .signature-art{display:block;width:150px;height:22px;margin:6px 0 4px;background:linear-gradient(90deg,#e6e6e6,#f4f4f4);border-radius:3px}
  .signer-name{font-size:13px;color:var(--ink);margin-bottom:2px}

  .footer-line{position:absolute;left:0;right:0;top:862px;display:flex;justify-content:center;align-items:center;gap:8px}
  .footer-line{top:auto;bottom:46px}
  .footer-dot{width:10px;height:10px;border-radius:50%;background:var(--tag-green)}
  .footer-text{font-family:"Open Sans",Arial,sans-serif;font-weight:600;font-size:13px;color:var(--ink)}

  /* Envelope front */
  .envelope-front{left:740px;top:330px;width:410px;height:214px}
  .envelope-front .edge-bar{width:4px}
  .envelope-front .brand-name{left:24px;top:18px;font-size:13px}
  .env-contact{position:absolute;left:24px;right:24px;top:176px;font-family:"Lato",Arial,sans-serif;font-size:8px;line-height:10px}
  .env-contact .line1{padding-bottom:4px;border-bottom:1px solid #c8c8c8;color:var(--ink)}
  .env-contact .line2{padding-top:4px;color:#222}

  /* Envelope back */
  .envelope-back{left:740px;top:580px;width:410px;height:214px}
  .flap{position:absolute;left:0;top:0;width:410px;height:50px}
  .faint-mark{position:absolute;left:0;right:0;top:100px;text-align:center;font-weight:700;font-size:36px;line-height:40px;color:#f8eeef}
</style>
</head>
<body>

<section class="sheet letterhead">
  <div class="edge-bar"></div>
  <div class="brand-name">Brindlecroft<br>Arcwell</div>
  <address class="contact-block">
    417 Harrowgate Lane<br>
    Ellsmoor, Vermont 05412
    <div class="gap"></div>
    <span class="label">P:</span> 802-555-0143<br>
    <span class="label">F:</span> 802-555-0144<br>
    <span class="web">www.BrindlecroftArcwell<span class="tld">.com</span></span>
  </address>

  <div class="letter-body">
    <p>Issuing Date: May 5, 2018</p>
    <p class="recipient">Name Of Employee Mr. XYZABC<br>Address of Employee<br>Address Line 2 etc..</p>
    <p style="margin-top:26px">Dear Mr.XYZABC</p>
    <p>Lorem Ipsum has been the industry's standard dummy text ever since the 1500s, when an unknown printer took a galley of type and scrambled it to make a type specimen book. It has survived not only five centuries, but also the leap into electronic typesetting, remaining essentially unchanged. It was popularised in the 1960s with the release of Letraset sheets containing Lorem Ipsum passages, and more recently with desktop publishing software like Aldus PageMaker including versions of Lorem Ipsum.</p>
    <p>Lorem Ipsum is simply dummy text of the printing and typesetting industry. Lorem Ipsum has been the industry's standard dummy text ever since the 1500s, when an unknown printer took a galley of type and scrambled it to make a type specimen book.</p>
    <p>It has survived not only five centuries, but also the leap into electronic typesetting, remaining essentially unchanged. It was popularised in the 1960s with the release of Letraset sheets containing Lorem Ipsum passages.</p>
    <p style="margin-bottom:0;margin-top:8px">Yours Sincerely</p>
    <span class="signature-art" role="img" aria-label="Handwritten signature"></span>
    <div class="signer-name">Dorian Halvey</div>
    <div>Managing Director</div>
  </div>

  <div class="footer-line">
    <span class="footer-dot"></span>
    <span class="footer-text">Powering a greener tomorrow</span>
  </div>
</section>

<section class="sheet envelope-front">
  <div class="edge-bar"></div>
  <div class="brand-name">Brindlecroft<br>Arcwell</div>
  <div class="env-contact">
    <div class="line1"><span class="label">P:</span> 802-555-0143 | <span class="label">F:</span> 802-555-0144 | <span style="color:var(--brand-red)">www.</span><span class="web">BrindlecroftArcwell</span><span style="color:var(--brand-red)">.com</span></div>
    <div class="line2">417 Harrowgate Lane Ellsmoor, Vermont 05412</div>
  </div>
</section>

<section class="sheet envelope-back">
  <svg class="flap" viewBox="0 0 410 50" preserveAspectRatio="none">
    <polygon points="0,0 410,0 398,50 12,50" fill="var(--brand-red)"/>
  </svg>
  <div class="faint-mark">Brindlecroft<br>Arcwell</div>
</section>

</body>
</html>
```